Brantor Works Business Card

Modern and Professional Business Card for a Med size construction/development company.

See the samples below for the design I like … but I need ideas for incorporating the red company logo while still keeping the clean look of the card samples that are attached.

Logo and tag line on the back … info on the front.

Tagline: Built Right from the First Footing

Target Market(s)

Med-Large General Contractors

Contact Information for Business Card

Brantor Works Limited
42 Felham Road
Lowbridge, NL
B3K 7T2

t: 709-555-0142
f: 709-555-0187
w: www.brantorworks-example.com

Font styles to use
Sans Serif

Colors
fbee3e

Requirements
Must have
• I like the black and yellow designs of the attached samples …. but I'm not sure how to incorporate the red Brantor Works logo into that design??
Nice to have
• Construction safety strips

```html
<!DOCTYPE html>
<html lang="en">
<head>
<meta charset="utf-8">
<title>Brantor Works Business Card</title>
<link rel="stylesheet" href="https://fonts.googleapis.com/css2?family=Arimo:wght@400;700&display=swap">
<style>
  :root {
    --stage: #3a3a3c;
    --brand-red: #e8222a;
    --ink: #2a2a2a;
    --ink-soft: #3c3c3c;
    --paper: #ffffff;
    --rule: #9a9a9a;
    --tag-line: #f3b8a8;
  }
  * { margin: 0; padding: 0; box-sizing: border-box; }
  html, body {
    width: 1200px; height: 1000px; overflow: hidden;
    background: var(--stage);
    font-family: "Arimo", Arial, sans-serif;
  }
  .sheet {
    position: relative; width: 1200px; height: 1000px;
    display: flex; flex-direction: column; align-items: center; justify-content: center; gap: 44px;
  }
  .card {
    position: relative; width: 760px; height: 434px;
    border-radius: 26px; overflow: hidden;
  }

  /* Back: name + tagline */
  .card-back {
    background: var(--brand-red);
    display: flex; flex-direction: column; align-items: center; justify-content: center;
  }
  .brand-name {
    color: var(--ink);
    font-weight: 700;
    font-size: 58px;
    letter-spacing: 1px;
    text-align: center;
    line-height: 1.05;
    text-transform: uppercase;
    white-space: nowrap;
  }
  .brand-name span { display: block; font-size: 30px; letter-spacing: 3px; margin-top: 8px; }
  .tagline {
    margin-top: 54px;
    padding: 10px 6px;
    border-top: 1.5px solid var(--tag-line);
    border-bottom: 1.5px solid var(--tag-line);
    color: var(--ink);
    font-weight: 700;
    font-size: 19px;
    letter-spacing: 1.5px;
    text-transform: uppercase;
    white-space: nowrap;
  }

  /* Front: contact info */
  .card-front {
    background: var(--paper);
    border-bottom: 12px solid var(--brand-red);
  }
  .identity {
    position: absolute; right: 382px; top: 150px;
    text-align: right; white-space: nowrap;
  }
  .person-name {
    color: var(--brand-red); font-weight: 700; font-size: 33px; letter-spacing: 0.5px; line-height: 1.1;
  }
  .person-role { color: var(--ink); font-size: 20px; margin-top: 2px; }
  .divider {
    position: absolute; left: 396px; top: 118px; width: 1.5px; height: 112px; background: var(--rule);
  }
  .contact-list {
    position: absolute; left: 414px; top: 126px; list-style: none;
  }
  .contact-list li {
    display: flex; align-items: center; gap: 8px;
    color: var(--ink-soft); font-size: 18px; line-height: 32px; white-space: nowrap;
  }
  .contact-list svg { width: 15px; height: 15px; flex: none; fill: var(--brand-red); }
  .address {
    position: absolute; left: 0; right: 0; bottom: 70px;
    text-align: center; color: var(--ink); font-size: 21px; white-space: nowrap;
  }
</style>
</head>
<body>
<main class="sheet">
  <section class="card card-back" aria-label="Card back">
    <h1 class="brand-name">Brantor Works<span>Limited</span></h1>
    <p class="tagline">Built Right from the First Footing</p>
  </section>

  <section class="card card-front" aria-label="Card front">
    <div class="identity">
      <h2 class="person-name">DALE MERCER</h2>
      <p class="person-role">Manager</p>
    </div>
    <div class="divider"></div>
    <ul class="contact-list">
      <li>
        <svg viewBox="0 0 16 16" aria-hidden="true"><path d="M3.5 1.5l2.6 0 1.2 3.4-1.7 1.2c.8 1.7 2.1 3 3.8 3.8l1.2-1.7 3.4 1.2 0 2.6c0 1-1 2-2 2C6.6 14 2 9.4 1.5 3.5c0-1 1-2 2-2z"/></svg>
        709-555-0142
      </li>
      <li>
        <svg viewBox="0 0 16 16" aria-hidden="true"><path d="M4 1h6l2 2v3H4z M2 7h12a1 1 0 0 1 1 1v6H1V8a1 1 0 0 1 1-1z M4 10v2h8v-2z" fill-rule="evenodd"/></svg>
        709-555-0187
      </li>
      <li>
        <svg viewBox="0 0 16 16" aria-hidden="true"><path d="M8 1a7 7 0 1 0 0 14A7 7 0 0 0 8 1zm0 2c1 1.2 1.6 3 1.6 5S9 11.8 8 13c-1-1.2-1.6-3-1.6-5S7 4.2 8 3zM3 7.3h10v1.4H3z" fill-rule="evenodd"/></svg>
        www.brantorworks-example.com
      </li>
    </ul>
    <p class="address">42 Felham Road, Lowbridge, NL&nbsp; B3K 7T2</p>
  </section>
</main>
</body>
</html>
```